Commercial janitorial cleaning

Janitorial cleaning particularly for commercial buildings. Website needs to specify free estimates. Location of service is Hudson, Valatie, East Greenbush, Troy, Albany ny area. Services page with Janitorial services- General Office Cleaning, Construction Cleaning, Carpet Extraction, Consultation/Business, Lighting Maintenance, Seasonal Deep Cleaning, Window cleaning, Event Cleaning, Floor and Carpet Cleaning, Floor Striping and Waxing. Contact us page with email phone number on page and a request page that emails me if they have any questions. About us page-the picture of my family on it with a section I can type a story myself.

Target Market(s)

Commercial businesses

Industry/Entity Type

Janitorial Service

Number of Pages Required

4 page

Font styles to use
Serif
Sans Serif
Script

Colors
ec1f27
1b1b1b
ffffff
9d9d9d

Requirements
Must have
• Phone number 555-314-2760. Must have free estimates on home page. Going for industrial / modern look to website
Nice to have
• Logo is a red and black building so if those colors could be coordinated to website that would be awesome.

```html
<!DOCTYPE html>
<html lang="en">
<head>
<meta charset="utf-8">
<title>Brightline Cleaning Services</title>
<link href="https://fonts.googleapis.com/css2?family=Lato:wght@400;700&family=Roboto:ital,wght@0,400;0,500;0,700;1,400&display=swap" rel="stylesheet">
<style>
:root{
  --red:#d7141c;
  --red-bright:#ec1f27;
  --ink:#1b1b1b;
  --white:#ffffff;
  --grey:#9d9d9d;
  --light:#efefef;
  --text:#555555;
}
*{box-sizing:border-box;margin:0;padding:0}
html,body{width:1200px;height:3158px;overflow:hidden}
body{font-family:'Roboto',sans-serif;color:var(--ink);background:var(--white);position:relative}
h1,h2,h3,h4{font-weight:400}
.abs{position:absolute}
.red{color:var(--red)}

/* header */
.hero{position:absolute;left:0;top:0;width:1200px;height:678px;
  background:linear-gradient(180deg,#6f7072 0%,#4a4b4d 45%,#2a2a2b 100%)}
.hero .shade{position:absolute;inset:0;background:radial-gradient(ellipse at 60% 60%,rgba(80,80,80,.2),rgba(0,0,0,.45))}
.topbar{position:absolute;left:0;top:0;width:1200px;height:137px;background:rgba(255,255,255,.82)}
.brand{position:absolute;left:82px;top:18px;width:130px;text-align:center;font-weight:700;font-size:12px;line-height:14px;color:var(--ink)}
.brand .mark{display:block;width:46px;height:46px;margin:0 auto 8px;background:var(--red)}
.call{position:absolute;right:80px;top:14px;display:flex;align-items:center;gap:12px;font-size:22px;color:var(--ink)}
.call .ring{width:58px;height:58px;border-radius:50%;background:var(--red);display:flex;align-items:center;justify-content:center}
.nav{position:absolute;top:80px;left:312px;display:flex;align-items:center;font-size:15.5px;color:#333}
.nav a{color:#333;text-decoration:none;padding:0 17px;line-height:44px}
.nav a.active{background:var(--red);color:#fff;border-radius:22px;padding:0 24px;margin-right:8px}
.hero-title{position:absolute;left:0;top:272px;width:1200px;text-align:center;font-family:'Lato',sans-serif;font-weight:700;font-size:58px;line-height:66px;color:#fff;text-transform:uppercase;letter-spacing:-.5px}
.hero-sub{position:absolute;left:0;top:422px;width:1200px;text-align:center;font-size:18px;color:#fff}
.btn{display:inline-block;border-radius:30px;font-size:19px;text-transform:uppercase;text-align:center;color:#fff}
.btn-red{background:var(--red)}
.btn-line{border:2px solid #fff}
.hero-btns{position:absolute;top:478px;left:0;width:1200px;display:flex;justify-content:center;gap:14px}
.hero-btns .btn{width:176px;line-height:58px}
.arrow{position:absolute;top:332px}

/* section heads */
.kicker{position:absolute;left:0;width:1200px;text-align:center;font-family:'Lato',sans-serif;font-size:20px;color:#444}
.heading{position:absolute;left:0;width:1200px;text-align:center;font-family:'Lato',sans-serif;font-weight:400;font-size:42px;color:var(--ink)}

/* welcome */
.welcome p{position:absolute;left:180px;width:840px;text-align:center;font-size:13.5px;line-height:28px;color:var(--text)}

/* services */
.services{position:absolute;left:0;top:1131px;width:1200px;height:679px;background:var(--light)}
.card{position:absolute;top:1356px;width:334px;height:385px;background:var(--red);border:2px solid var(--red)}
.card .photo{height:208px}
.card h3{font-size:23px;color:#fff;text-align:center;margin-top:24px}
.card p{font-size:13.5px;line-height:25px;color:#fff;text-align:center;padding:0 26px;margin-top:12px}
.badge{position:absolute;top:1310px;width:84px;height:84px;border-radius:50%;background:var(--red);display:flex;align-items:center;justify-content:center}

/* estimate */
.estimate{position:absolute;left:0;top:1810px;width:1200px;height:426px;
  background:linear-gradient(90deg,#1e1e1e 0%,#2c2c2c 50%,#555047 100%)}
.estimate h2{position:absolute;left:78px;top:52px;font-size:42px;color:#fff}
.estimate .lead{position:absolute;left:78px;top:110px;width:680px;font-size:13.5px;line-height:25px;color:#bdbdbd}
.field{position:absolute;width:333px;height:53px;border:1px solid #8a8a8a;background:rgba(255,255,255,.08);color:#ddd;font-size:14px;padding:17px 14px}
.submit{position:absolute;left:78px;top:2113px;width:674px;height:55px;border-radius:28px;background:var(--red);color:#fff;font-size:20px;text-align:center;line-height:55px}

/* testimonial */
.quote{position:absolute;left:240px;top:2415px;width:720px;text-align:center;font-style:italic;font-size:14px;line-height:29px;color:var(--text)}
.client{position:absolute;left:0;top:2568px;width:1200px;text-align:center;font-size:16px;font-weight:700;color:var(--red)}

/* email band */
.emailband{position:absolute;left:0;top:2646px;width:1200px;height:158px;background:var(--red)}
.emailband h2{position:absolute;left:132px;top:40px;font-family:'Lato',sans-serif;font-size:40px;color:var(--ink)}
.emailband em{position:absolute;left:134px;top:92px;font-size:15px;color:var(--ink)}
.emailband .input{position:absolute;left:459px;top:40px;width:378px;height:55px;background:#f2f2f2;font-size:13px;color:#888;padding:20px 16px}
.emailband .sub{position:absolute;left:886px;top:40px;width:168px;height:56px;line-height:52px;border:2px solid #fff;border-radius:28px;color:#fff;font-size:20px;text-align:center}

/* footer */
.footer{position:absolute;left:0;top:2804px;width:1200px;height:290px;background:var(--ink);color:#ddd}
.fbrand{position:absolute;left:110px;top:70px;width:190px;text-align:center;font-weight:700;font-size:22px;line-height:28px;color:var(--red)}
.fbrand .mark{display:block;width:70px;height:70px;margin:0 auto 14px;background:var(--red)}
.social{position:absolute;top:186px;left:120px;display:flex;gap:14px}
.social span{width:46px;height:46px;border-radius:50%;border:2px solid #9d9d9d}
.social span.on{background:var(--red);border-color:var(--red)}
.fcol{position:absolute;top:44px}
.fcol h4{font-size:16px;font-weight:500;color:var(--red);margin-bottom:18px}
.links li{list-style:none;font-size:13.5px;line-height:27px;color:#ddd}
.links li:before{content:'›';color:var(--red);margin-right:14px;font-size:18px}
.touch .row{display:flex;gap:16px;font-size:13.5px;line-height:22px;margin-bottom:18px}
.touch .row b{font-weight:400;color:var(--red)}
.news p{font-size:13.5px;line-height:24px;width:250px}
.news .input{width:250px;height:42px;background:#f2f2f2;color:#555;font-size:13px;padding:13px 10px;margin-top:14px}
.news .sub{width:154px;line-height:46px;border-radius:24px;background:var(--red);color:#fff;font-size:20px;text-align:center;margin-top:10px}
.copy{position:absolute;left:0;top:3094px;width:1200px;height:64px;background:var(--red);text-align:center;line-height:64px;font-size:15px;color:var(--ink)}
</style>
</head>
<body>

<header>
  <div class="hero" role="img" aria-label="Photo of a hallway being vacuumed with a cleaning cart"><div class="shade"></div></div>
  <div class="topbar"></div>
  <div class="brand"><span class="mark"></span>Brightline<br>Cleaning Services</div>
  <div class="call">Call Us On
    <span class="ring"><svg width="28" height="28" viewBox="0 0 24 24"><path fill="#fff" d="M6.6 10.8a15.1 15.1 0 0 0 6.6 6.6l2.2-2.2c.3-.3.7-.4 1-.2 1.1.4 2.3.6 3.6.6.6 0 1 .4 1 1V20c0 .6-.4 1-1 1C10.6 21 3 13.4 3 4c0-.6.4-1 1-1h3.5c.6 0 1 .4 1 1 0 1.3.2 2.5.6 3.6.1.3 0 .7-.2 1z"/></svg></span>
    555-314-2760</div>
  <nav class="nav">
    <a class="active">HOME</a><a>ABOUT US</a><a>SERVICES</a><a>EMAIL ME</a><a>FREE ESTIMATE</a><a>BLOG</a><a>CONTACT US</a>
  </nav>
  <svg class="arrow" style="left:26px" width="30" height="60" viewBox="0 0 30 60"><path d="M26 2 4 30l22 28" fill="none" stroke="#fff" stroke-width="2"/></svg>
  <svg class="arrow" style="right:26px" width="30" height="60" viewBox="0 0 30 60"><path d="M4 2l22 28L4 58" fill="none" stroke="#fff" stroke-width="2"/></svg>
  <h1 class="hero-title">We keep your world fresh<br>and sparkling clean.</h1>
  <p class="hero-sub">Lorem Ipsum is simply dummy text of the printing and typesetting industry.</p>
  <div class="hero-btns"><span class="btn btn-red">Know More</span><span class="btn btn-line">Contact Us</span></div>
</header>

<section class="welcome">
  <div class="kicker" style="top:738px">Welcome to</div>
  <h2 class="heading" style="top:772px">Brightline <span class="red">Cleaning Services</span></h2>
  <p style="top:842px">Lorem Ipsum is simply dummy text of the printing and typesetting industry. Lorem Ipsum has been the industry's standard dummy text ever since the 1500s, when an unknown printer took a galley of type and scrambled it to make a type specimen sum has been the industry's standard dummy text ever since the 1500s, when an unknown printer took a galley.</p>
  <p style="top:936px">It has survived not only five centuries, but also the leap into electronic typesetting, remaining essentially unchanged. It was popularised in the 1960s with the release of Letraset sheets containing</p>
  <span class="btn btn-red abs" style="left:511px;top:1013px;width:178px;line-height:58px">Know More</span>
</section>

<section class="services"></section>
<div class="kicker" style="top:1192px">We Provide You</div>
<h2 class="heading" style="top:1222px">Our Best <span class="red">Services</span></h2>

<article class="card" style="left:78px">
  <div class="photo" role="img" aria-label="Photo of an office floor being mopped beside a wet floor sign" style="background:linear-gradient(135deg,#b9bcc0,#7d8590 60%,#c9b24a)"></div>
  <h3>General Office Cleaning</h3>
  <p>Lorem Ipsum is simply dummy text of the printing and typesetting industry. Lorem Ipsum has been the industry's standard.</p>
</article>
<article class="card" style="left:434px">
  <div class="photo" role="img" aria-label="Photo of a freshly finished room with a step ladder" style="background:linear-gradient(135deg,#e8e8e6,#c9c9c7 60%,#a9a9a6)"></div>
  <h3>Construction Cleaning</h3>
  <p>Lorem Ipsum is simply dummy text of the printing and typesetting industry. Lorem Ipsum has been the industry's stand.</p>
</article>
<article class="card" style="left:789px">
  <div class="photo" role="img" aria-label="Photo of a large hall floor being polished" style="background:linear-gradient(180deg,#7a7a76,#b7b8b4 55%,#d8d9d6)"></div>
  <h3>Floor and Carpet Cleaning</h3>
  <p>Lorem Ipsum is simply dummy text of the printing and typesetting industry. Lorem Ipsum has been the industry's standard.</p>
</article>
<div class="badge" style="left:203px"><svg width="44" height="44" viewBox="0 0 24 24"><circle cx="11" cy="4" r="2.2" fill="#fff"/><path d="M9 7h4l1 6-2 1v7h-2v-7l-2-1z M15 9l5 11" fill="#fff" stroke="#fff" stroke-width="1.2"/></svg></div>
<div class="badge" style="left:558px"><svg width="44" height="44" viewBox="0 0 24 24"><circle cx="9" cy="5" r="2.2" fill="#fff"/><path d="M7 8h4l2 5-2 1-1-2v8H8v-6l-2 3-2-1z M13 20l5-8 4 8z" fill="#fff"/></svg></div>
<div class="badge" style="left:913px"><svg width="44" height="44" viewBox="0 0 24 24"><path d="M8 20a5 5 0 0 1 10 0z M13 15V6a3 3 0 0 0-6 0v2" fill="#fff" stroke="#fff" stroke-width="1.6"/></svg></div>

<section class="estimate" role="img" aria-label="Photo of a cleaning in progress sign on a dark floor">
  <h2>Get A <span style="color:var(--red-bright)">Free Estimate</span></h2>
  <p class="lead">Lorem Ipsum is simply dummy text of the printing and typesetting industry. Lorem Ipsum has been the industry's standard dummy text ever since the</p>
</section>
<div class="field" style="left:78px;top:1985px">Name*</div>
<div class="field" style="left:419px;top:1985px">Phone*</div>
<div class="field" style="left:78px;top:2046px">Email*</div>
<div class="field" style="left:419px;top:2046px">Message*</div>
<div class="submit">SUBMIT</div>

<section class="testimonials">
  <div class="kicker" style="top:2297px">Testimonials</div>
  <h2 class="heading" style="top:2330px">What Our <span class="red">Client Say</span></h2>
  <svg class="abs" style="left:200px;top:2408px" width="26" height="22" viewBox="0 0 26 22"><path d="M0 22V12C0 5 4 1 10 0v4c-3 1-5 4-5 7h5v11zm14 0V12c0-7 4-11 10-12v4c-3 1-5 4-5 7h5v11z" fill="var(--red)"/></svg>
  <p class="quote">Lorem Ipsum is simply dummy text of the printing and typesetting industry. Lorem Ipsum has been the industry's standard dummy text ever since the 1500s, when an unknown printer took a galley of type and scrambled it to make a</p>
  <svg class="abs" style="left:958px;top:2482px" width="26" height="22" viewBox="0 0 26 22"><path d="M26 0v10c0 7-4 11-10 12v-4c3-1 5-4 5-7h-5V0zM12 0v10c0 7-4 11-10 12v-4c3-1 5-4 5-7H2V0z" fill="var(--red)"/></svg>
  <svg class="abs" style="left:230px;top:2512px" width="740" height="40" viewBox="0 0 740 40"><path d="M0 8h345l-12 22 28-22h379" fill="none" stroke="#e0777b" stroke-width="2" stroke-dasharray="6 4"/></svg>
  <div class="client">CLIENT NAME</div>
</section>

<section class="emailband">
  <h2>Email Me</h2>
  <em>You have any questions Keep in Touch</em>
  <div class="input">Enter Your Email</div>
  <svg class="abs" style="left:836px;top:58px" width="20" height="20" viewBox="0 0 24 24"><path d="M2 12 22 3l-5 18-5-6-6 3 2-6z" fill="none" stroke="var(--red)" stroke-width="2"/></svg>
  <div class="sub">SUBSCRIBE</div>
</section>

<footer class="footer">
  <div class="fbrand"><span class="mark"></span>Brightline</div>
  <div class="social"><span class="on"></span><span></span><span></span></div>
  <div class="fcol" style="left:346px">
    <h4>USEFULL LINKS</h4>
    <ul class="links"><li>Home</li><li>About Us</li><li>Services</li><li>Email Me</li><li>Free Estimate</li><li>Contact Us</li></ul>
  </div>
  <div class="fcol touch" style="left:609px;width:250px">
    <h4>GET IN TOUCH</h4>
    <div class="row"><svg width="18" height="24" viewBox="0 0 18 24"><path d="M9 0a9 9 0 0 0-9 9c0 7 9 15 9 15s9-8 9-15a9 9 0 0 0-9-9zm0 12a3 3 0 1 1 0-6 3 3 0 0 1 0 6z" fill="var(--red)"/></svg><div><b>Brightline Cleaning<br>Services</b><br>Millbrook, Cedar Falls, Ridgeway</div></div>
    <div class="row"><svg width="18" height="18" viewBox="0 0 24 24"><path fill="var(--red)" d="M6.6 10.8a15.1 15.1 0 0 0 6.6 6.6l2.2-2.2c.3-.3.7-.4 1-.2 1.1.4 2.3.6 3.6.6.6 0 1 .4 1 1V20c0 .6-.4 1-1 1C10.6 21 3 13.4 3 4c0-.6.4-1 1-1h3.5c.6 0 1 .4 1 1 0 1.3.2 2.5.6 3.6.1.3 0 .7-.2 1z"/></svg>555-314-2760</div>
    <div class="row"><svg width="20" height="16" viewBox="0 0 20 16"><rect width="20" height="16" rx="2" fill="var(--red)"/><path d="M1 2l9 7 9-7" fill="none" stroke="#1b1b1b" stroke-width="1.6"/></svg>office@brightline.com</div>
  </div>
  <div class="fcol news" style="left:874px">
    <h4>NEWSLETTER</h4>
    <p>Would you like to receive exclusive access to articles, white papers and our regular monthly newsletter?</p>
    <div class="input">Enter Email Id</div>
    <div class="sub">SUBSCRIBE</div>
  </div>
</footer>
<div class="copy">© Brightline Cleaning Services - 2017. All Rights Reserved</div>

</body>
</html>
```